Web-Redesign für Anbieter von immersiver Medienproduktion, Virtual Reality und 360-Grad-Aufnahmen
Zielgruppe
Bei dem Auftrag geht es um ein ReDesign der bestehende Website www.lumorix7.de
Lumorix 7 ist ein Powerhouse für immersive Medienproduktion, Virtual Reality und 360 Grad Aufnahmen. Wir erschaffen faszinierende und verblüffende Customer Experiences über alle Kanäle hinweg. Unsere Markeninszenierungen sind immer am Rande des technisch machbaren und hinterlassen nachhaltigen Eindruck beim Kunden. Dabei ist die Verbindung von hochwertigem Design, cutting-edge Technology und Emotion der Kern unserer Arbeit. Wir sind digital und real. Und Experten darin, Marken neuartig erfahrbar und damit erfolgreich zu machen. Nationale und internationale Kunden aus den Bereichen Automotive, Pharma, TV und Industrie vertrauen uns seit vielen Jahren.
Aufgabenstellung
Wir möchten unseren Slogan 'WE DO THE NEW' in den Fokus stellen und den Fokus auf uns Showreell samt 'Über uns'-Text legen. Wir wollen innovativ, futuristisch und aber klar strukturiert sein. Unser Ziel ist es, ein Termin mit dem potentiellen Interessenten zu haben.

```html
<!DOCTYPE html>
<html lang="de">
<head>
<meta charset="utf-8">
<title>Lumorix 7 – We do the new</title>
<link href="https://fonts.googleapis.com/css2?family=Barlow:wght@400;500;600;700&family=Barlow+Semi+Condensed:wght@600;700&display=swap" rel="stylesheet">
<style>
:root{
  --bg:#062a5d;
  --bg-deep:#05224d;
  --panel-top:#174a86;
  --panel-bot:#0c3670;
  --line:#2e5f9c;
  --white:#ffffff;
  --muted:#c9d7ee;
  --video-dark:#2a0d08;
  --video-gold:#8a5a1c;
}
*{box-sizing:border-box;margin:0;padding:0}
html,body{width:1200px;height:3132px;overflow:hidden}
body{background:var(--bg);color:var(--white);font-family:'Barlow',sans-serif;position:relative}
.abs{position:absolute}
.heading{font-family:'Barlow Semi Condensed',sans-serif;font-weight:700;letter-spacing:.5px}

/* top bar */
.topbar{left:101px;top:12px;width:998px;height:27px;background:var(--white);border-radius:8px;box-shadow:0 0 10px rgba(120,170,255,.5);display:flex;align-items:center;justify-content:space-between;padding:0 12px;color:#123;font-size:10px;font-weight:500}
.social{display:flex;gap:5px}
.social span{width:16px;height:16px;border-radius:50%;background:var(--bg)}

/* header */
.brand{font-weight:700;font-size:21px;letter-spacing:1px;display:flex;align-items:center;gap:6px}
.brand i{display:inline-block;width:22px;height:22px;border-radius:50%;background:var(--white)}
.site-brand{left:106px;top:62px}
.nav{right:106px;top:73px;display:flex;gap:25px;font-size:11px;font-weight:600;letter-spacing:.5px}

/* hero */
.hero{left:100px;top:110px;width:1000px;height:560px}
.hero-title{left:195px;top:360px;font-size:38px}
.showreel{left:861px;top:358px;width:145px;height:45px;border:2px solid var(--white);border-radius:6px;background:var(--bg);box-shadow:0 0 0 2px var(--bg);display:flex;align-items:center;justify-content:center;font-size:12px;font-weight:700;letter-spacing:1.5px}

/* panels */
.panel{background:linear-gradient(160deg,var(--panel-top),var(--panel-bot));border:1.5px solid var(--line);border-radius:20px}
.icon-box{width:49px;height:49px;border-radius:9px;background:var(--bg);box-shadow:0 0 8px rgba(120,170,255,.55);display:flex;align-items:center;justify-content:center;font-weight:700;font-size:24px}
.about{left:106px;top:732px;width:987px;height:232px}
.about .icon-box{position:absolute;left:38px;top:47px}
.about h2{position:absolute;left:38px;top:111px;font-size:38px}
.about p{position:absolute;left:361px;top:50px;width:590px;font-size:10px;line-height:15px;font-weight:500}

.section-title{left:0;width:1200px;text-align:center;font-size:38px}

.service h3{font-size:24px;margin:18px 0 10px}
.service p{font-size:10px;line-height:15px;font-weight:500}
.service{width:595px}

/* clients */
.client{width:190px;height:111px;border-radius:8px;background:linear-gradient(160deg,var(--panel-top),var(--panel-bot));box-shadow:0 0 10px rgba(120,170,255,.5);display:flex;align-items:center;justify-content:center;font-weight:700;font-size:21px;top:2398px}
.arrow{top:2440px;font-size:22px}

/* contact */
.contact-left{left:106px;top:2606px;width:337px;height:191px}
.contact-left .icon-box{position:absolute;left:38px;top:48px}
.contact-left h2{position:absolute;left:38px;top:112px;font-size:38px}
.contact-form{left:456px;top:2606px;width:637px;height:293px}
.field{position:absolute;left:40px;width:558px;border:1.5px solid var(--white);border-radius:5px;background:var(--bg);font-size:10px;color:var(--muted);padding:8px 11px}
.send{position:absolute;left:40px;top:205px;width:558px;height:37px;background:var(--white);border-radius:5px;color:var(--bg);font-size:12px;font-weight:600;letter-spacing:2px;display:flex;align-items:center;justify-content:center}

/* footer */
.footer-line{left:0;top:2970px;width:1200px;height:1px;background:var(--line)}
.footer-col{top:3012px;font-size:9px;line-height:12px;font-weight:500}
.footer-col h4{font-size:12px;font-weight:600;letter-spacing:.5px;margin-bottom:12px}
.footer-col a{color:var(--white);text-decoration:underline;display:block}
.to-top{left:1148px;top:3092px;width:20px;height:20px;border-radius:50%;background:var(--white);color:var(--bg);font-size:11px;display:flex;align-items:center;justify-content:center}
</style>
</head>
<body>

<div class="abs topbar"><span>Lichtbogenweg 7, 82049 Pullach</span><div class="social"><span></span><span></span><span></span></div></div>

<div class="abs brand site-brand">LUMORIX <i></i></div>
<nav class="abs nav"><span>HOME</span><span>ÜBER UNS</span><span>SERVICES</span><span>KONTAKT</span><span>TERMIN</span></nav>

<svg class="abs hero" viewBox="0 0 1000 560" aria-hidden="false">
  <defs>
    <linearGradient id="videoGrad" x1="0" y1="0" x2="1" y2="1">
      <stop offset="0" stop-color="#3a2a18"/>
      <stop offset=".45" stop-color="#8a5a1c"/>
      <stop offset=".6" stop-color="#5a1a10"/>
      <stop offset="1" stop-color="#1e1410"/>
    </linearGradient>
  </defs>
  <rect x="0" y="0" width="1000" height="560" fill="#082c60"/>
  <rect x="25" y="21" width="949" height="511" rx="40" fill="#0b3469" stroke="#3b6fb0" stroke-width="2"/>
  <rect x="50" y="46" width="899" height="464" rx="28" fill="url(#videoGrad)" role="img" aria-label="Showreel-Standbild: prunkvolles Tor mit goldenen Ornamenten"/>
  <path d="M362 44 C400 44 395 76 430 76 L570 76 C605 76 600 44 638 44 Z" fill="#0b3469"/>
  <path d="M362 512 C400 512 395 476 430 476 L570 476 C605 476 600 512 638 512 Z" fill="#0b3469"/>
</svg>
<div class="abs heading hero-title">WE DO THE NEW.</div>
<div class="abs showreel">SHOWREEL →</div>

<section class="abs panel about">
  <div class="icon-box">7</div>
  <h2 class="heading">ÜBER UNS</h2>
  <p>Lumorix 7 ist ein Powerhouse für immersive Medienproduktion, Virtual Reality und 360 Grad Aufnahmen. Wir erschaffen faszinierende und verblüffende Customer Experiences über alle Kanäle hinweg. Unsere Markeninszenierungen sind immer am Rande des technisch machbaren und hinterlassen nachhaltigen Eindruck beim Kunden. Dabei ist die Verbindung von hochwertigem Design, cutting-edge Technology und Emotion der Kern unserer Arbeit. Wir sind digital und real. Und Experten darin, Marken neuartig erfahrbar und damit erfolgreich zu machen. Nationale und internationale Kunden aus den Bereichen Automotive, Pharma, TV und Industrie vertrauen uns seit vielen Jahren.<br><br>Kommen Sie zu uns, wir können Zukunft.</p>
</section>

<h2 class="abs heading section-title" style="top:1015px">SERVICES</h2>

<svg class="abs" style="left:0;top:1080px" width="430" height="330" viewBox="0 0 430 330" role="img" aria-label="Foto: Performer mit Sonnenbrille vor Kamerateams, Schriftzug Design &amp; Content Creation">
  <defs><linearGradient id="s1" x1="0" y1="0" x2="1" y2="0"><stop offset="0" stop-color="#5c6c9a"/><stop offset=".6" stop-color="#8a92c0"/><stop offset="1" stop-color="#c7cbe6"/></linearGradient></defs>
  <path d="M0 60 H340 Q358 60 365 78 L420 300 Q424 326 398 326 H0 Z" fill="url(#s1)"/>
</svg>
<div class="abs service" style="left:511px;top:1150px">
  <div class="icon-box"><svg width="22" height="22" viewBox="0 0 22 22"><circle cx="11" cy="11" r="9" fill="none" stroke="#fff" stroke-width="2"/><rect x="5" y="9" width="12" height="5" rx="2" fill="#fff"/></svg></div>
  <h3 class="heading">DESIGN &amp; CONTENT CREATION</h3>
  <p>Wir entwickeln starke Marken und füllen sie mit Leben, um Ihre Marken und Produkte unwiderstehlich zu machen. Wir glauben an klares, einprägsames und hochwertiges Design, das die Kraft emotionaler Geschichten nutzt. Dabei beobachten wir das Markenumfeld und suchen immer nach neuen Wegen, um Ihre Zielgruppe zu erreichen – über Kopf UND Herz. Unsere Expertise umfasst Design für TV-Sender und TV-Formate, TV-Kampagnen, Messebespielungen, Imagefilme, Werbespots und Social Media Filme.</p>
</div>

<div class="abs service" style="left:94px;top:1547px">
  <div class="icon-box"><svg width="24" height="14" viewBox="0 0 24 14"><rect x="1" y="1" width="22" height="11" rx="3" fill="#fff"/></svg></div>
  <h3 class="heading">REALTIME EXPERIENCES</h3>
  <p>Sie planen eine Veranstaltung, Messe oder ein besonders Corporate Event auszurichten? Ein Event, welches eine beeindruckende, immersive Erfahrung bietet? Dann lassen Sie uns sprechen. Seit über 20 Jahren arbeiten wir in der professionellen Event-Planung im Bereich Immersive Events. Wir kreieren Ereignisse, die den Zuschauer faszinieren und ihn mittels neuester Technologien in eine andere Welt abtauchen lassen.</p>
</div>
<svg class="abs" style="left:776px;top:1475px" width="424" height="320" viewBox="0 0 424 320" role="img" aria-label="Foto: Person mit VR-Brille in futuristischer Halle, Schriftzug Realtime Experiences">
  <defs><linearGradient id="s2" x1="0" y1="0" x2="1" y2="0"><stop offset="0" stop-color="#5f8c92"/><stop offset=".5" stop-color="#b9c6c4"/><stop offset="1" stop-color="#3a6676"/></linearGradient></defs>
  <path d="M85 52 H424 V317 H22 Q0 317 4 295 L60 70 Q66 52 85 52 Z" fill="url(#s2)"/>
</svg>

<svg class="abs" style="left:0;top:1848px" width="428" height="334" viewBox="0 0 428 334" role="img" aria-label="Foto: Mann mit VR-Brille und erhobenen Händen, Schriftzug Video Performance Marketing">
  <defs><linearGradient id="s3" x1="0" y1="0" x2="1" y2="0"><stop offset="0" stop-color="#c4506a"/><stop offset=".45" stop-color="#2a2a32"/><stop offset="1" stop-color="#b8803a"/></linearGradient></defs>
  <path d="M0 68 H340 Q358 68 364 86 L420 306 Q424 332 398 332 H0 Z" fill="url(#s3)"/>
</svg>
<div class="abs service" style="left:511px;top:1942px">
  <div class="icon-box"><svg width="14" height="22" viewBox="0 0 14 22"><rect x="4" y="1" width="4" height="11" rx="2" fill="#fff"/><rect x="2" y="9" width="11" height="11" rx="4" fill="#fff"/></svg></div>
  <h3 class="heading">VIDEO PERFORMANCE MARKETING</h3>
  <p>Performance TV-Marketing rückt Artikel, die der Zuschauer entdeckt hat, in unmittelbare Interaktionsnähe des Kunden. Denn fast jeder zweite Zuschauer sucht online nach Produkten, die er kurz zuvor im Fernsehen gesehen hat. Richtig abgeholt, wird aus der Recherche ein Verkaufserfolg. Genau darauf sind wir spezialisiert.</p>
</div>

<div class="abs icon-box" style="left:575px;top:2274px"><svg width="26" height="16" viewBox="0 0 26 16"><circle cx="13" cy="4" r="3.5" fill="#fff"/><circle cx="5" cy="6" r="2.6" fill="#fff"/><circle cx="21" cy="6" r="2.6" fill="#fff"/><rect x="7" y="9" width="12" height="6" rx="3" fill="#fff"/><rect x="0" y="10" width="9" height="5" rx="2.5" fill="#fff"/><rect x="17" y="10" width="9" height="5" rx="2.5" fill="#fff"/></svg></div>
<h2 class="abs heading section-title" style="top:2325px">KUNDEN</h2>
<div class="abs arrow" style="left:110px">←</div>
<div class="abs client" style="left:135px">Preisfalke</div>
<div class="abs client" style="left:382px">Klarblick</div>
<div class="abs client" style="left:627px">Nordwelle Media</div>
<div class="abs client" style="left:876px">Alpenfunk</div>
<div class="abs arrow" style="left:1070px">→</div>

<section class="abs panel contact-left">
  <div class="icon-box"><svg width="24" height="22" viewBox="0 0 24 22"><ellipse cx="12" cy="9" rx="10" ry="7.5" fill="none" stroke="#fff" stroke-width="2"/><path d="M6 15 L4 21 L11 16" fill="#fff"/></svg></div>
  <h2 class="heading">KONTAKT</h2>
</section>
<form class="abs panel contact-form">
  <div class="field" style="top:48px;height:37px">Name</div>
  <div class="field" style="top:93px;height:37px">Email</div>
  <div class="field" style="top:137px;height:61px;padding-top:5px">Nachricht</div>
  <div class="send">SENDEN</div>
</form>

<div class="abs footer-line"></div>
<div class="abs footer-col" style="left:106px;top:3008px">
  <div class="brand" style="margin-bottom:14px">LUMORIX <i></i></div>
  <p>© 2023 LUMORIX7. Alle Rechte vorbehalten. <u>Cookie-<br>Richtlinie (EU)</u> / <u>Haftungsausschluss</u> / <u>Impressum</u></p>
</div>
<div class="abs footer-col" style="left:356px"><h4>KONTAKT</h4><p>Lumorix 7<br>Lichtbogenweg 7<br>82049 Pullach</p></div>
<div class="abs footer-col" style="left:607px"><h4>PARTNER LINKS</h4><a>Jonas Wendt Kreativstudio</a><a>Moosbote</a><a>Dreiklang Medien Service</a></div>
<div class="abs footer-col" style="left:856px"><h4>QUICK LINKS</h4><a>Über uns</a><a>Services</a><a>Kontakt</a></div>
<div class="abs to-top">↑</div>

</body>
</html>
```